QUILLMERE, INC. BUSINESS CARD REDESIGN

Attached is an example business card. Name, Title, Address, Contact Information, logo and social media icons are ALL required to be designed into the card. The logo can be modified. An exact replica (or few modifications) of the existing design will be rejected.

Card can either have a blue or white background. Blues and any complimentary color of social media logos that are included on the card.

An example is attached/provided but should not be merely copied or slightly modified.

This should be a new, innovative design relative to the general concept of the existing business card.

Reason: This project has been updated; please utilize the original logo as much as possible. Also because of the high quality of most of the submissions the company requires additional time to reach out with feedback to the top designers for editing and re-submission to determine the finalist. Thank you.

Target Market(s)

B2B (business to business), Television News Stations, Broadcasting, Radio, Magazine and Newspaper Organizations.

Industry/Entity Type

Media

Contact Information for Business Card

Example attached. Company name with exisiting logo (can be altered/edited) in blue (similar to chirplo/pagewall blue, but brighter and/or bolder).

Optional two sided card so that just the "QUILLMERE" logo is on the front side of the card with contact information on the back side.

Logo Text

QUILLMERE

Font styles to use
Sans Serif
Other font styles liked:
• ubuntu, ubuntu bold etc...or similar clean fonts that look great on mobile. Open to use of Google Fonts.

Requirements
Must have
• Must have the following branding integrated into the design (not in any specefic order or verbatim):
• QUILLMERE, INC.
• Delwyn Harrop CEO & Founder
• 88 Lindenmere Nashville, TN 37594
• mobile: 615.472.3016
• delwyn@quillmere-demo.com
• https://quillmere-demo.com
• Must also include brand assests (e.g. official logos) of CHIRPLO, PAGEWALL, VIDTROVE, TACKWELLO, LUMIGRIDZ, and FLEETPIK
• A clean logo only on the front side is requested (blue or white background). The front side can incorporate the social media icons listed in the brief if designer chooses.
Nice to have
• Card can either have a blue or white background. Blues and any complimentary color of social media logos that are included on the card.
• The card can be double sided so that the logo is on front and contact information is professionally displayed on the back. Not necessarily a requirement but a double-sided design will receive a higher preference.
• An example is attached/provided but should not be merely copied or slightly modified.
• This should be a new, innovative design relative to the general concept of the existing business card.
• Also the brand name with the TM trademark after: for example, Quillmere™
• This (the tm) should be added only after a standalone use of just the word QUILLMERE or Quillmere™ AND not Quillmere™, Inc., included in the URL or email address obviously. Thanks :)
Should not have
• Should not have the text spelling of Pagewall, Lumigridz, Tackwello, Fleetpik, etc...with the exception of "VidTrove" as it is the approved logo to be integrated.

```html
<!DOCTYPE html>
<html lang="en">
<head>
<meta charset="utf-8">
<title>Quillmere Business Card</title>
<link href="https://fonts.googleapis.com/css2?family=Ubuntu:wght@400;500;700&display=swap" rel="stylesheet">
<style>
  :root {
    --brand-blue: #0b0bf0;
    --paper: #ffffff;
    --backdrop: #2a2a2a;
    --ink: #1c1c1c;
    --muted: #555555;
    --pagewall: #0d5aa0;
    --tackwello: #e0222a;
    --chirplo: #1ea6ea;
    --lumigridz: #e0407a;
    --vidtrove: #e8231b;
    --fleetpik: #f5d000;
  }
  * { box-sizing: border-box; margin: 0; padding: 0; }
  html, body { width: 1200px; height: 1200px; overflow: hidden; }
  body {
    background: var(--backdrop);
    font-family: "Ubuntu", sans-serif;
    color: var(--ink);
    position: relative;
  }
  .card {
    position: absolute;
    left: 130px;
    width: 940px;
    height: 537px;
    background: var(--paper);
    overflow: hidden;
  }
  .card--back { top: 42px; }
  .card--front { top: 621px; }

  /* Back side */
  .side-block {
    position: absolute; left: 0; top: 110px; width: 95px; height: 190px;
    background: var(--brand-blue);
  }
  .brand-lockup {
    position: absolute; left: 120px; top: 80px; width: 160px;
    display: flex; flex-direction: column; align-items: center; gap: 14px;
  }
  .brand-lockup__mark {
    width: 84px; height: 84px; background: var(--brand-blue); border-radius: 8px;
  }
  .brand-lockup__name {
    font-weight: 700; font-size: 30px; color: var(--brand-blue); letter-spacing: 0.5px;
  }
  .name-band {
    position: absolute; left: 300px; top: 60px; right: 0; height: 190px;
    background: var(--brand-blue); color: var(--paper);
    padding: 50px 0 0 140px;
  }
  .name-band__name { font-weight: 700; font-size: 50px; line-height: 1.1; }
  .name-band__title { font-weight: 400; font-size: 21px; margin-top: 8px; }

  .contact-list {
    position: absolute; left: 460px; top: 282px; list-style: none;
    display: flex; flex-direction: column; gap: 14px;
  }
  .contact-list__item {
    display: flex; align-items: center; gap: 22px; font-size: 29px; color: var(--ink);
  }
  .contact-list__icon { width: 32px; height: 32px; flex: none; display: flex; align-items: center; justify-content: center; }
  .contact-list__at { font-size: 34px; color: var(--muted); line-height: 1; }
  .address {
    position: absolute; left: 460px; top: 442px;
    display: flex; align-items: center; gap: 22px;
  }
  .address__company { font-size: 29px; font-weight: 400; }
  .address__street { font-size: 21px; margin-top: 2px; }

  /* Front side */
  .front-band {
    position: absolute; left: 0; right: 0; top: 225px; height: 180px;
    background: var(--brand-blue);
  }
  .front-mark {
    position: absolute; left: 352px; top: 175px; width: 236px; height: 236px;
    background: var(--brand-blue); border-radius: 14px;
    box-shadow: 0 0 0 18px var(--paper);
  }
  .front-wordmark {
    position: absolute; left: 0; right: 0; top: 422px; text-align: center;
    font-weight: 700; font-size: 72px; line-height: 1; color: var(--brand-blue); letter-spacing: 1px;
  }

  .social {
    position: absolute; display: flex; align-items: center; gap: 12px;
    font-size: 20px; font-weight: 500; color: var(--vidtrove);
  }
  .social__dot { width: 60px; height: 60px; border-radius: 50%; flex: none; }
  .social--pagewall { left: 153px; top: 135px; }
  .social--pagewall .social__dot { background: var(--pagewall); }
  .social--tackwello { left: 292px; top: 66px; }
  .social--tackwello .social__dot { background: var(--tackwello); }
  .social--chirplo { left: 457px; top: 66px; }
  .social--chirplo .social__dot { background: var(--chirplo); }
  .social--lumigridz { left: 614px; top: 118px; }
  .social--lumigridz .social__dot { background: var(--lumigridz); }
  .social--fleetpik { left: 640px; top: 30px; }
  .social--fleetpik .social__dot { background: var(--fleetpik); }
  .social--vidtrove { left: 740px; top: 140px; }
  .social--vidtrove .social__dot { background: var(--vidtrove); }
</style>
</head>
<body>

<section class="card card--back" aria-label="Card back: contact details">
  <div class="side-block"></div>
  <div class="brand-lockup">
    <div class="brand-lockup__mark"></div>
    <div class="brand-lockup__name">quillmere</div>
  </div>
  <div class="name-band">
    <h1 class="name-band__name">Delwyn Harrop</h1>
    <p class="name-band__title">CEO &amp; Founder</p>
  </div>
  <ul class="contact-list">
    <li class="contact-list__item">
      <span class="contact-list__icon">
        <svg width="22" height="32" viewBox="0 0 22 32" fill="none" stroke="#555" stroke-width="2.5"><rect x="2" y="2" width="18" height="28" rx="3"/><circle cx="11" cy="25" r="1.5" fill="#555"/></svg>
      </span>
      615.472.3016
    </li>
    <li class="contact-list__item">
      <span class="contact-list__icon"><span class="contact-list__at">@</span></span>
      delwyn@quillmere-demo.com
    </li>
    <li class="contact-list__item">
      <span class="contact-list__icon">
        <svg width="32" height="32" viewBox="0 0 32 32" fill="none" stroke="#555" stroke-width="2"><circle cx="16" cy="16" r="13"/><ellipse cx="16" cy="16" rx="6" ry="13"/><line x1="3" y1="16" x2="29" y2="16"/><line x1="5" y1="9" x2="27" y2="9"/><line x1="5" y1="23" x2="27" y2="23"/></svg>
      </span>
      https://quillmere-demo.com
    </li>
  </ul>
  <div class="address">
    <span class="contact-list__icon">
      <svg width="26" height="34" viewBox="0 0 26 34"><path d="M13 1C6.4 1 1 6.2 1 12.6 1 21 13 33 13 33s12-12 12-20.4C25 6.2 19.6 1 13 1z" fill="#333"/><circle cx="13" cy="12.5" r="4.5" fill="#fff"/></svg>
    </span>
    <div>
      <p class="address__company">QUILLMERE, INC.</p>
      <p class="address__street">88 Lindenmere Nashville, TN 37594</p>
    </div>
  </div>
</section>

<section class="card card--front" aria-label="Card front: brand">
  <div class="front-band"></div>
  <div class="front-mark"></div>
  <div class="front-wordmark">quillmere</div>

  <div class="social social--pagewall" aria-label="Pagewall"><span class="social__dot"></span></div>
  <div class="social social--tackwello" aria-label="Tackwello"><span class="social__dot"></span></div>
  <div class="social social--chirplo" aria-label="Chirplo"><span class="social__dot"></span></div>
  <div class="social social--lumigridz" aria-label="Lumigridz"><span class="social__dot"></span></div>
  <div class="social social--fleetpik" aria-label="Fleetpik"><span class="social__dot"></span></div>
  <div class="social social--vidtrove"><span class="social__dot"></span>VidTrove</div>
</section>

</body>
</html>
```